Power point design for a financial seminar

I would like to receive 10 designed power point slides with the same look & feel that should related to finance since its for a seminar related to stock markets and economics. Please note that texts are in Hebrew (translate is attached in a Word document).
There should be background with upper and bottom layers similar to all to include the attached logo.
All slides should have a Title and some of the slides should have designed bullets and other generic graphic elements that we will use in our presentation.
Please note that text should be right to left so texts will be aligned to the right and graphics at the left/upper/bottom
Target Market(s)
Youngsters
Look and feel
Each slider illustrates characteristics of the customer's brand and the style your logo design should communicate.

```html
<!DOCTYPE html>
<html lang="he" dir="rtl">
<head>
<meta charset="utf-8">
<title>קורס שוק ההון - בסיס</title>
<link href="https://fonts.googleapis.com/css2?family=Heebo:wght@300;400;500;700&family=Lato:wght@400;700&display=swap" rel="stylesheet">
<style>
:root{
  --blue:#2f7fd0;
  --blue-dark:#1d5fa6;
  --sky:#4aa3e6;
  --ink:#2d3440;
  --muted:#7a828e;
  --line:#dde3ea;
  --card:#ffffff;
  --page:#eef1f5;
  --money-a:#8fa68d;
  --money-b:#c7d3c2;
  --brand:#6aa84f;
}
*{box-sizing:border-box;margin:0;padding:0}
html,body{width:1200px;height:4136px;overflow:hidden}
body{background:var(--page);font-family:"Heebo",sans-serif;color:var(--ink);position:relative}
.slide{position:absolute;width:480px;height:270px;background:var(--card);box-shadow:0 4px 14px rgba(30,50,80,.12);overflow:hidden}
.slide.left{left:100px}.slide.right{left:620px}
.title-slide{left:100px;top:100px;width:1000px;height:560px}
.h{position:absolute;right:22px;top:22px;font-size:24px;font-weight:500;line-height:1.15;text-align:right}
.accent{position:absolute;right:22px;width:40px;height:3px;background:var(--blue)}
.photo{position:absolute}
.money{background:linear-gradient(135deg,var(--money-a),var(--money-b) 60%,#9db29a)}
.office{background:linear-gradient(135deg,#6d7c8c,#b9c4cf)}
.dark{background:linear-gradient(135deg,#1e2a38,#3b4d63)}
.mark{position:absolute;left:14px;bottom:10px;display:flex;align-items:center;gap:5px;font-size:9px;font-weight:500;color:var(--brand)}
.mark i{width:14px;height:14px;border-radius:50%;border:2px solid var(--brand);display:block}
.p{position:absolute;font-size:9px;line-height:1.45;color:var(--muted);text-align:right}
.box{position:absolute;background:#fff;border:1px solid var(--line);font-size:9px;display:flex;align-items:center;justify-content:center;text-align:center;color:var(--ink)}
.box.on{background:var(--blue);color:#fff;border-color:var(--blue)}
.bluebox{position:absolute;background:var(--blue);color:#fff}
.grid8{position:absolute;left:14px;right:14px;bottom:36px;height:96px;display:grid;grid-template-columns:repeat(4,1fr);grid-template-rows:1fr 1fr;gap:6px}
.grid8 .box{position:static}
</style>
</head>
<body>

<!-- title -->
<section class="slide title-slide">
  <div class="mark" style="left:460px;top:130px;bottom:auto;font-size:16px;gap:8px"><i style="width:34px;height:34px;border-width:3px"></i>מנטור הון</div>
  <h1 style="position:absolute;width:100%;top:300px;text-align:center;font-size:38px;font-weight:500">קורס שוק ההון- בסיס (חדש)</h1>
  <p style="position:absolute;width:100%;top:360px;text-align:center;font-size:16px;color:var(--muted)">של לביא</p>
  <div style="position:absolute;left:470px;top:395px;width:60px;height:3px;background:var(--blue)"></div>
</section>

<!-- row 1 -->
<section class="slide left" style="top:688px">
  <div class="photo office" style="inset:0" role="img" aria-label="תמונת הרצאה בכיתה"></div>
  <div style="position:absolute;inset:0;background:rgba(47,127,208,.55)"></div>
  <div class="h" style="color:#fff;top:110px;right:110px;font-size:20px">קורס שוק ההון בסיס (חדש)</div>
</section>
<section class="slide right" style="top:688px">
  <div style="position:absolute;left:60px;top:80px;width:60px;height:3px;background:var(--blue)"></div>
  <div style="position:absolute;right:40px;top:90px;font-family:Lato,sans-serif;font-size:34px;font-weight:700;direction:ltr">Welcome</div>
  <div class="p" style="right:40px;top:140px;width:220px">ברוכים הבאים לקורס שוק ההון</div>
  <div class="mark"><i></i>מנטור הון</div>
</section>

<!-- row 2 -->
<section class="slide left" style="top:998px">
  <div class="h">רקע על המרצה</div>
  <div class="accent" style="top:56px"></div>
  <div class="box" style="right:14px;top:70px;width:140px;height:46px">ניסיון בשוק ההון</div>
  <div class="box" style="right:160px;top:70px;width:140px;height:46px">ייעוץ השקעות</div>
  <div class="box" style="right:306px;top:70px;width:140px;height:46px">הרצאות וסדנאות</div>
  <div class="photo office" style="right:14px;top:124px;width:140px;height:104px" role="img" aria-label="תמונת המרצה"></div>
  <div class="photo office" style="right:160px;top:124px;width:140px;height:104px" role="img" aria-label="תמונת קהל בסדנה"></div>
  <div class="photo office" style="right:306px;top:124px;width:140px;height:104px" role="img" aria-label="תמונת כיתת לימוד"></div>
  <div class="mark"><i></i>מנטור הון</div>
</section>
<section class="slide right" style="top:998px">
  <div class="photo dark" style="left:0;top:0;width:200px;height:270px" role="img" aria-label="מסך גרפים של מסחר"></div>
  <div class="h">בורסה</div>
  <div class="bluebox" style="right:22px;top:64px;width:240px;height:160px;padding:14px;font-size:9px;line-height:1.9;text-align:right">
    • שוק מאורגן למסחר בניירות ערך<br>• מפגש בין קונים למוכרים<br>• קביעת מחיר לפי ביקוש והיצע<br>• פיקוח של רשות ניירות ערך<br>• מסחר בימי חול בשעות קבועות<br>• גיוס הון לחברות ציבוריות
  </div>
  <div class="mark"><i></i>מנטור הון</div>
</section>

<!-- row 3 -->
<section class="slide left" style="top:1308px">
  <div class="photo dark" style="left:0;top:0;width:260px;height:270px" role="img" aria-label="לוח מסחר כהה"></div>
  <div class="h">ני"ע נסחרים<br>בבורסה</div>
  <div class="bluebox" style="left:20px;top:150px;width:60px;height:60px;font-size:9px;display:flex;align-items:center;justify-content:center">מניות</div>
  <div class="bluebox" style="left:88px;top:150px;width:60px;height:60px;font-size:9px;display:flex;align-items:center;justify-content:center">אג"ח</div>
  <div class="bluebox" style="left:156px;top:150px;width:60px;height:60px;font-size:9px;display:flex;align-items:center;justify-content:center">קרנות</div>
  <div class="bluebox" style="left:224px;top:150px;width:60px;height:60px;font-size:9px;display:flex;align-items:center;justify-content:center">אופציות</div>
  <div class="mark"><i></i>מנטור הון</div>
</section>
<section class="slide right" style="top:1308px">
  <div class="photo office" style="left:0;top:0;width:190px;height:270px" role="img" aria-label="שולחן עבודה עם מחשב"></div>
  <div class="h">מדדים</div>
  <div class="accent" style="top:56px"></div>
  <div class="p" style="right:22px;top:74px;width:240px;line-height:1.9">
    <b style="color:var(--blue)">מדד מניות מוביל</b><br>מדד המשקלל את החברות הגדולות בבורסה ומשקף את מגמת השוק הכללית.<br>• מדדי ענף ומדדי אג"ח<br>• מדדים בינלאומיים מובילים
  </div>
  <div class="mark"><i></i>מנטור הון</div>
</section>

<!-- rows 4-8: influence on share price -->
<section class="slide left" style="top:1618px">
  <div class="photo money" style="left:0;top:0;width:210px;height:120px" role="img" aria-label="שטרות כסף"></div>
  <div class="h">השפעה על מחיר המנייה</div>
  <div class="p" style="left:14px;top:126px;width:200px">הריבית במשק משפיעה על כדאיות ההשקעה במניות.</div>
  <div class="grid8"><div class="box on">ריבית</div><div class="box">אינפלציה</div><div class="box">דוחות כספיים</div><div class="box">מצב המשק</div><div class="box">שער חליפין</div><div class="box">חדשות</div><div class="box">ביקוש והיצע</div><div class="box">דיבידנד</div></div>
  <div class="mark"><i></i>מנטור הון</div>
</section>
<section class="slide right" style="top:1618px">
  <div class="photo money" style="left:0;top:0;width:210px;height:120px" role="img" aria-label="שטרות כסף"></div>
  <div class="h">השפעה על מחיר המנייה</div>
  <div class="p" style="left:14px;top:126px;width:200px">עליית מחירים שוחקת את ערך הכסף והרווחים.</div>
  <div class="grid8"><div class="box">ריבית</div><div class="box on">אינפלציה</div><div class="box">דוחות כספיים</div><div class="box">מצב המשק</div><div class="box">שער חליפין</div><div class="box">חדשות</div><div class="box">ביקוש והיצע</div><div class="box">דיבידנד</div></div>
  <div class="mark"><i></i>מנטור הון</div>
</section>

<section class="slide left" style="top:1928px">
  <div class="photo money" style="left:0;top:0;width:210px;height:120px" role="img" aria-label="שטרות כסף"></div>
  <div class="h">השפעה על מחיר המנייה</div>
  <div class="p" style="left:14px;top:126px;width:200px">תוצאות רבעוניות טובות מעלות את הביקוש למניה.</div>
  <div class="grid8"><div class="box">ריבית</div><div class="box">אינפלציה</div><div class="box on">דוחות כספיים</div><div class="box">מצב המשק</div><div class="box">שער חליפין</div><div class="box">חדשות</div><div class="box">ביקוש והיצע</div><div class="box">דיבידנד</div></div>
  <div class="mark"><i></i>מנטור הון</div>
</section>
<section class="slide right" style="top:1928px">
  <div class="photo money" style="left:0;top:0;width:210px;height:120px" role="img" aria-label="שטרות כסף"></div>
  <div class="h">השפעה על מחיר המנייה</div>
  <div class="p" style="left:14px;top:126px;width:200px">צמיחה במשק תומכת ברווחי החברות ובמחירן.</div>
  <div class="grid8"><div class="box">ריבית</div><div class="box">אינפלציה</div><div class="box">דוחות כספיים</div><div class="box on">מצב המשק</div><div class="box">שער חליפין</div><div class="box">חדשות</div><div class="box">ביקוש והיצע</div><div class="box">דיבידנד</div></div>
  <div class="mark"><i></i>מנטור הון</div>
</section>

<section class="slide left" style="top:2238px">
  <div class="photo money" style="left:0;top:0;width:210px;height:120px" role="img" aria-label="שטרות כסף"></div>
  <div class="h">השפעה על מחיר המנייה</div>
  <div class="p" style="left:14px;top:126px;width:200px">שינוי במטבע משפיע על חברות יצואניות ויבואניות.</div>
  <div class="grid8"><div class="box">ריבית</div><div class="box">אינפלציה</div><div class="box">דוחות כספיים</div><div class="box">מצב המשק</div><div class="box on">שער חליפין</div><div class="box">חדשות</div><div class="box">ביקוש והיצע</div><div class="box">דיבידנד</div></div>
  <div class="mark"><i></i>מנטור הון</div>
</section>
<section class="slide right" style="top:2238px">
  <div class="photo money" style="left:0;top:0;width:210px;height:120px" role="img" aria-label="שטרות כסף"></div>
  <div class="h">השפעה על מחיר המנייה</div>
  <div class="p" style="left:14px;top:126px;width:200px">אירועים וחדשות יוצרים תנודות חדות במחיר.</div>
  <div class="grid8"><div class="box">ריבית</div><div class="box">אינפלציה</div><div class="box">דוחות כספיים</div><div class="box">מצב המשק</div><div class="box">שער חליפין</div><div class="box on">חדשות</div><div class="box">ביקוש והיצע</div><div class="box">דיבידנד</div></div>
  <div class="mark"><i></i>מנטור הון</div>
</section>

<section class="slide left" style="top:2548px">
  <div class="photo money" style="left:0;top:0;width:210px;height:120px" role="img" aria-label="שטרות כסף"></div>
  <div class="h">השפעה על מחיר המנייה</div>
  <div class="p" style="left:14px;top:126px;width:200px">המחיר נקבע במפגש בין הקונים למוכרים.</div>
  <div class="grid8"><div class="box">ריבית</div><div class="box">אינפלציה</div><div class="box">דוחות כספיים</div><div class="box">מצב המשק</div><div class="box">שער חליפין</div><div class="box">חדשות</div><div class="box on">ביקוש והיצע</div><div class="box">דיבידנד</div></div>
  <div class="mark"><i></i>מנטור הון</div>
</section>
<section class="slide right" style="top:2548px">
  <div class="photo money" style="left:0;top:0;width:210px;height:120px" role="img" aria-label="שטרות כסף"></div>
  <div class="h">השפעה על מחיר המנייה</div>
  <div class="p" style="left:14px;top:126px;width:200px">חלוקת רווחים לבעלי המניות משפיעה על המחיר.</div>
  <div class="grid8"><div class="box">ריבית</div><div class="box">אינפלציה</div><div class="box">דוחות כספיים</div><div class="box">מצב המשק</div><div class="box">שער חליפין</div><div class="box">חדשות</div><div class="box">ביקוש והיצע</div><div class="box on">דיבידנד</div></div>
  <div class="mark"><i></i>מנטור הון</div>
</section>

<section class="slide left" style="top:2858px">
  <div class="photo money" style="left:0;top:0;width:210px;height:120px" role="img" aria-label="שטרות כסף"></div>
  <div class="h">השפעה על מחיר המנייה</div>
  <div class="p" style="left:14px;top:126px;width:200px">ציפיות המשקיעים לעתיד מתומחרות מראש.</div>
  <div class="grid8"><div class="box">ריבית</div><div class="box">אינפלציה</div><div class="box">דוחות כספיים</div><div class="box">מצב המשק</div><div class="box">שער חליפין</div><div class="box">חדשות</div><div class="box">ביקוש והיצע</div><div class="box">דיבידנד</div></div>
  <div class="mark"><i></i>מנטור הון</div>
</section>
<section class="slide right" style="top:2858px">
  <div class="photo money" style="left:0;top:0;width:210px;height:120px" role="img" aria-label="שטרות כסף"></div>
  <div class="h">השפעה על מחיר המנייה</div>
  <div class="p" style="left:14px;top:126px;width:200px">שילוב כל הגורמים יוצר את מחיר השוק.</div>
  <div class="grid8"><div class="box">ריבית</div><div class="box">אינפלציה</div><div class="box">דוחות כספיים</div><div class="box">מצב המשק</div><div class="box">שער חליפין</div><div class="box">חדשות</div><div class="box">ביקוש והיצע</div><div class="box">דיבידנד</div></div>
  <div class="mark"><i></i>מנטור הון</div>
</section>

<!-- row 9 -->
<section class="slide left" style="top:3168px">
  <div class="h">פרמטרים להשקעה</div>
  <div class="photo office" style="left:40px;top:60px;width:140px;height:140px;border-radius:50%" role="img" aria-label="צמח בעציץ על שולחן"></div>
  <div class="p" style="right:22px;top:70px;width:230px;line-height:2;color:var(--ink)">
    <b>רמת סיכון</b><br>• טווח ההשקעה<br>• תשואה צפויה<br>• נזילות<br>• פיזור ההשקעות
  </div>
  <div class="mark"><i></i>מנטור הון</div>
</section>
<section class="slide right" style="top:3168px">
  <div class="h" style="top:110px">איך להשקיע</div>
  <svg style="position:absolute;left:30px;top:20px" width="230" height="230" viewBox="0 0 230 230">
    <g font-family="Heebo" font-size="11" fill="#fff" text-anchor="middle">
      <path d="M115 20 A95 95 0 0 1 210 115 L160 115 A45 45 0 0 0 115 70 Z" fill="#2f7fd0"/>
      <path d="M210 115 A95 95 0 0 1 115 210 L115 160 A45 45 0 0 0 160 115 Z" fill="#4aa3e6"/>
      <path d="M115 210 A95 95 0 0 1 20 115 L70 115 A45 45 0 0 0 115 160 Z" fill="#1d5fa6"/>
      <path d="M20 115 A95 95 0 0 1 115 20 L115 70 A45 45 0 0 0 70 115 Z" fill="#6bb7ee"/>
      <text x="160" y="65">תיק עצמאי</text><text x="160" y="175">קרנות</text>
      <text x="70" y="175">יועץ</text><text x="70" y="65">מנהל תיקים</text>
    </g>
  </svg>
  <div class="mark"><i></i>מנטור הון</div>
</section>

<!-- row 10 -->
<section class="slide left" style="top:3478px">
  <div class="h" style="top:90px">נושאים<br>מתקדמים</div>
  <svg style="position:absolute;left:20px;top:30px" width="220" height="210" viewBox="0 0 220 210">
    <g font-family="Heebo" font-size="9" fill="#fff" text-anchor="middle">
      <polygon points="110,10 145,30 145,70 110,90 75,70 75,30" fill="#2f7fd0"/><text x="110" y="54">גידור</text>
      <polygon points="70,80 105,100 105,140 70,160 35,140 35,100" fill="#4aa3e6"/><text x="70" y="124">מינוף</text>
      <polygon points="150,80 185,100 185,140 150,160 115,140 115,100" fill="#1d5fa6"/><text x="150" y="124">שורט</text>
      <polygon points="110,120 145,140 145,180 110,200 75,180 75,140" fill="#6bb7ee"/><text x="110" y="164">ניתוח טכני</text>
    </g>
  </svg>
  <div class="mark"><i></i>מנטור הון</div>
</section>
<section class="slide right" style="top:3478px">
  <div class="h" style="top:90px">נגזרים<br>פיננסיים</div>
  <div class="bluebox" style="left:40px;top:110px;width:110px;height:36px;font-size:10px;display:flex;align-items:center;justify-content:center">אופציות</div>
  <svg style="position:absolute;left:160px;top:116px" width="24" height="24" viewBox="0 0 24 24"><path d="M4 12h16M14 6l6 6-6 6" stroke="#2d3440" stroke-width="2" fill="none"/></svg>
  <div style="position:absolute;left:190px;top:118px;font-size:10px">חוזים עתידיים</div>
  <div class="mark"><i></i>מנטור הון</div>
</section>

<!-- row 11 -->
<section class="slide left" style="top:3788px">
  <div class="photo office" style="left:0;top:0;width:170px;height:270px" role="img" aria-label="איש עסקים הולך ברחוב"></div>
  <div class="h">איש קשר</div>
  <div class="p" style="right:22px;top:62px;width:250px">לשאלות ופרטים נוספים ניתן לפנות אלינו בכל עת.</div>
  <div class="p" style="right:22px;top:200px;width:250px;color:var(--ink);line-height:1.7">רון לביא<br>050-0000000 | info@mentor-hon.co.il</div>
  <div class="mark" style="left:180px"><i></i>מנטור הון</div>
</section>
<section class="slide right" style="top:3788px">
  <div class="photo office" style="inset:0" role="img" aria-label="משרד פתוח עם עובדים"></div>
  <div style="position:absolute;right:40px;top:0;width:150px;height:270px;background:rgba(47,127,208,.8)"></div>
  <div class="h" style="color:#fff;right:60px;top:180px;font-size:26px">תודה</div>
</section>

</body>
</html>
```